Web design for Zembrolia.com

We need a website (4 starter pages) designed for a drupal based site. The theme is flexible so I am open to different designs/looks. I am looking for a VERY simple and clean and FUN design to make it easy to use for the customer.

Our company is similar to Kelvo pact as in it's for multiple people to design a cake for a customer and they choose a winning design and work with that cake designer to make the cake (birthday, wedding etc...)

Our vision:
First page:
2 main images for either the customer to submit an idea for a cake, or the new designer to sign up to the site. Perhaps a mouse-over with wording on what the options are? You can use this site:
http://www.plindorfy.com/ as a sort of template but more clean and simple

"How it works" page:
Similar to this:
http://www.plindorfy.com/how-it-works
Fun, clean and simple

Submit cake design page (form submission)

Submit new designer page

Ideally a 960 wide design with no flash, but open to a flash design if it stands out...

Please contact me if you have any questions!

People who want a custom cake made, and people who design and make cakes.

Wedding

• Use the logo attached. The "Oven Mit" should be a big part of the site...kind of a site mascot?
• 960 wide
No flash but not a deal-breaker if there is flash and it's amazing...

```html
<!DOCTYPE html>
<html lang="en">
<head>
<meta charset="utf-8">
<title>Zembrolia.com – Home</title>
<link rel="stylesheet" href="https://fonts.googleapis.com/css2?family=Ubuntu:wght@400;500;700&family=Mulish:ital,wght@0,300;0,400;1,800&display=swap">
<style>
:root{
  --page:#ede6da;
  --brown:#964409;
  --brown-light:#b0703a;
  --tab:#b06a3c;
  --button-top:#b98a70;
  --button-bottom:#a06c52;
  --yellow:#f5b820;
  --ribbon:#f7a823;
  --heading:#8c4a12;
  --text:#555555;
  --dark:#444444;
  --white:#ffffff;
}
*{margin:0;padding:0;box-sizing:border-box}
html,body{width:1000px;height:1200px;overflow:hidden}
body{background:var(--page);font-family:"Ubuntu",sans-serif;position:relative}
.abs{position:absolute}

/* top bar */
.topbar{left:39px;top:22px;width:921px;height:40px;background:var(--brown);border-bottom:6px solid var(--brown-light);box-sizing:content-box}
.topbar .phone{position:absolute;left:12px;top:8px}
.topbar .call{position:absolute;left:52px;top:9px;color:#f7e4c8;font-size:12px}
.topbar .call strong{font-size:17px;font-weight:500;letter-spacing:.3px;margin-left:2px}
.topbar .cart{position:absolute;right:60px;top:14px;color:#f3dcc0;font-size:11px}
.topbar .cart-icon{position:absolute;right:20px;top:4px}

/* header */
.sheet{left:39px;top:68px;width:921px;height:1035px;background:var(--white)}
.logo{left:52px;top:104px;display:flex;align-items:center;gap:8px;font-family:"Ubuntu",sans-serif;font-weight:700;font-size:28px;color:var(--brown)}
.logo .mark{width:20px;height:20px;border-radius:50%;background:var(--tab)}
.search{left:781px;top:88px;width:166px;height:23px;border:1px solid #bbb;border-radius:3px;background:#fff}
.search svg{position:absolute;left:6px;top:4px}
.nav{left:306px;top:119px;width:654px;height:34px;display:flex;align-items:center;font-size:14.5px;font-weight:500}
.nav a{color:var(--brown);text-decoration:none;padding:0 23px;height:34px;line-height:36px}
.nav a.active{background:var(--tab);color:#fff;border-radius:8px 8px 0 0;padding:0 18px}
.nav a:last-child{padding-right:13px}
.navline{left:39px;top:153px;width:921px;height:2px;background:var(--brown)}

/* hero */
.hero{left:39px;top:155px;width:921px;height:188px;display:flex}
.hero div{height:100%}

/* tagline */
.tagline{left:0;top:362px;width:1000px;text-align:center;font-family:"Mulish",sans-serif;font-weight:300;font-size:30px;line-height:36px;color:var(--heading);padding-left:10px}
.tagline em{font-style:italic;font-weight:800}
.tagline .gold{color:var(--yellow)}

/* specials */
.specials{left:39px;top:471px;width:921px;height:239px;background:var(--brown);border-bottom:6px solid var(--brown-light);box-sizing:content-box}
.ribbon{left:10px;top:464px}
.special{position:absolute;top:18px;width:250px}
.special h3{color:var(--yellow);font-size:18px;font-weight:500;text-align:center;margin-left:-4px}
.special .photo{width:158px;height:118px;border:3px solid var(--yellow);margin:5px 0 0 42px;background:#fff}
.special p{color:#fff;font-family:Arial,sans-serif;font-size:12px;line-height:14.5px;margin-top:12px}
.special .more{display:block;text-align:right;color:var(--yellow);font-family:Arial,sans-serif;font-size:12px;margin-top:1px;margin-right:-1px}
.arrow{top:585px}

/* sidebar */
.categories{left:52px;top:735px;width:245px}
.categories h2{font-size:18px;font-weight:500;color:var(--heading);padding-left:18px;padding-bottom:9px;border-bottom:1px solid var(--brown-light)}
.categories ul{list-style:none;padding-left:20px;margin-top:14px}
.categories li{font-size:14px;font-weight:500;color:var(--text);height:30px;line-height:20px;letter-spacing:.2px}
.btn-side{left:46px;width:273px;height:43px;border-radius:8px;color:#fff;font-size:18px;font-weight:500;padding-left:20px;line-height:43px;letter-spacing:.3px}
.btn-idea{top:981px;background:linear-gradient(var(--button-top),var(--button-bottom));border:1px solid #8a5a42}
.btn-sign{top:1042px;background:var(--tab)}
.btn-sign span{color:var(--ribbon)}

/* main */
.welcome{left:360px;top:739px;width:560px}
.welcome h1{font-size:18px;font-weight:500;color:var(--dark);letter-spacing:.4px}
.welcome p{font-family:Verdana,sans-serif;font-size:11px;line-height:14.5px;color:var(--text);margin-top:14px}
.welcome p:first-of-type{margin-top:26px}
.welcome p.narrow{width:340px;height:72px;overflow:hidden;white-space:nowrap}
.welcome p.narrow span{display:block;overflow:hidden}
.piping{left:740px;top:925px;width:220px;height:178px;background:linear-gradient(120deg,#3fa7e6 0%,#f39a3c 30%,#6fce5a 50%,#f07fb5 72%,#f5d43a 100%);clip-path:polygon(10% 40%,60% 0,100% 0,100% 100%,8% 100%)}
.read-more{left:634px;top:1064px;width:87px;height:22px;border-radius:7px;background:linear-gradient(#ffe76a,#f5b820);border:1px solid #d79a12;color:#5a3a05;font-size:12px;font-weight:500;text-align:center;line-height:20px}

/* footer */
.footnav{right:42px;top:1113px;display:flex;gap:0;font-size:12.5px;font-weight:500}
.footnav a{color:var(--brown);text-decoration:none;margin-left:35px}
.footnav a:first-child{color:var(--dark)}
.copyright{left:53px;top:1161px;font-family:Verdana,sans-serif;font-size:10px;font-weight:700;color:var(--dark)}
.social{left:836px;top:1156px;display:flex;gap:3px}
.social span{width:28px;height:28px;border-radius:4px}
</style>
</head>
<body>

<header class="abs topbar">
  <svg class="phone" width="24" height="24" viewBox="0 0 24 24" aria-hidden="true">
    <circle cx="12" cy="12" r="10.5" fill="none" stroke="#f7e4c8" stroke-width="1.5"/>
    <path d="M9 6.5c-1.5.5-2 2-1.5 4 .8 3 2.8 5.5 5.5 7 1.6.8 3 .4 3.6-.8l-2-2-1.4.7c-1.3-.8-2.4-2.2-3-3.7l1.2-1L9 6.5z" fill="#f7e4c8"/>
  </svg>
  <div class="call">Call us - <strong>0044 712 9083</strong></div>
  <div class="cart">Your cart is empty</div>
  <svg class="cart-icon" width="32" height="30" viewBox="0 0 32 30" aria-hidden="true">
    <path d="M2 4h5l4 15h15l3-11H9" fill="none" stroke="#dde4e8" stroke-width="2"/>
    <circle cx="13" cy="24" r="2.2" fill="#dde4e8"/><circle cx="24" cy="24" r="2.2" fill="#dde4e8"/>
    <path d="M17 13h8v-3l5 5-5 5v-3h-8z" fill="#5ab832"/>
  </svg>
</header>

<div class="abs sheet"></div>

<div class="abs logo"><span class="mark"></span>Zembrolia.com</div>

<div class="abs search">
  <svg width="14" height="14" viewBox="0 0 14 14" aria-hidden="true"><circle cx="5.5" cy="5.5" r="4" fill="none" stroke="#333" stroke-width="2"/><path d="M8.5 8.5l4 4" stroke="#333" stroke-width="2.2"/></svg>
</div>

<nav class="abs nav">
  <a class="active" href="#">Home</a><a href="#">About us</a><a href="#">Products</a><a href="#">Specials</a><a href="#">Reviews</a><a href="#">FAQs</a><a href="#">Contact us</a>
</nav>
<div class="abs navline"></div>

<section class="abs hero">
  <div role="img" aria-label="Three-tier white cake with black damask pattern" style="width:141px;background:linear-gradient(#1e1e1e,#d8d4cc 60%,#777)"></div>
  <div role="img" aria-label="Pink iced cupcake topped with a cherry" style="width:160px;background:linear-gradient(135deg,#f2c6cf,#e48fa6 60%,#c9a274)"></div>
  <div role="img" aria-label="Striped green and pink tiered cake with flowers" style="width:111px;background:linear-gradient(#f1eee0,#b7c48a 50%,#6e8a4a)"></div>
  <div role="img" aria-label="White cake covered in sugar roses" style="width:120px;background:linear-gradient(#f4f1ec,#d9d3c6)"></div>
  <div role="img" aria-label="Pink cupcakes on a spotted tablecloth" style="width:132px;background:linear-gradient(#e7b6c4,#df7d9a 60%,#c2456a)"></div>
  <div role="img" aria-label="Green tiered cake with white dots and bow" style="width:117px;background:linear-gradient(#f1f1ea,#9dc25c 55%,#5e8a33)"></div>
  <div role="img" aria-label="Bright multicoloured tiered party cake" style="width:140px;background:linear-gradient(160deg,#111,#e05a3a 40%,#f2c12e 70%,#d83c8a)"></div>
</section>

<p class="abs tagline">It is all about our <em>customer needs</em> thus,<br>we <span class="gold">cater for a <em>wide variety of occasions</em></span></p>

<section class="abs specials">
  <article class="special" style="left:55px">
    <h3>Wedding cakes</h3>
    <div class="photo" role="img" aria-label="Croissant on a plate" style="background:linear-gradient(#c7b39a,#e39a4a 50%,#f2efe9)"></div>
    <p>Lorem ipsum dolor sit amet, consectetuer adipis cing elit. Praesent vestibulum molestie lacus.</p>
    <a class="more" href="#">Read more...</a>
  </article>
  <article class="special" style="left:346px">
    <h3>Graduation cakes</h3>
    <div class="photo" role="img" aria-label="Chocolate brownie slices with white drizzle" style="background:linear-gradient(135deg,#f4f0ea,#5a2a1a 40%,#3a160c)"></div>
    <p>Lorem ipsum dolor sit amet, consectetuer adipis cing elit. Praesent vestibulum molestie lacus.</p>
    <a class="more" href="#">Read more...</a>
  </article>
  <article class="special" style="left:657px">
    <h3>Christening cakes</h3>
    <div class="photo" role="img" aria-label="Layered dessert slice on a white plate" style="background:linear-gradient(#2e2a26,#d7c39e 55%,#f4f2ee)"></div>
    <p>Lorem ipsum dolor sit amet, consectetuer adipis cing elit. Praesent vestibulum molestie lacus.</p>
    <a class="more" href="#">Read more...</a>
  </article>
</section>

<svg class="abs ribbon" width="182" height="84" viewBox="0 0 182 84" aria-label="Specials">
  <path d="M168 7l14 8h-12z" fill="#6a2e06"/>
  <path d="M2 44L168 7l10 9L30 80z" fill="var(--ribbon)"/>
  <text x="80" y="47" transform="rotate(-22 80 47)" text-anchor="middle" fill="#fff" font-family="Georgia,serif" font-size="17">SPECIALS</text>
</svg>

<svg class="abs arrow" style="left:57px" width="16" height="26" viewBox="0 0 16 26" aria-hidden="true"><path d="M13 2L3 13l10 11" fill="none" stroke="#5a2806" stroke-width="3"/></svg>
<svg class="abs arrow" style="left:922px" width="16" height="26" viewBox="0 0 16 26" aria-hidden="true"><path d="M3 2l10 11L3 24" fill="none" stroke="#5a2806" stroke-width="3"/></svg>

<aside class="abs categories">
  <h2>Categories</h2>
  <ul>
    <li>Wedding cakes</li>
    <li>Birthday cakes</li>
    <li>Corporate cakes &amp; cupcakes</li>
    <li>Graduation cakes</li>
    <li>Christening cakes</li>
    <li>Any celebration</li>
  </ul>
</aside>
<a class="abs btn-side btn-idea">Submit an idea for a cake</a>
<a class="abs btn-side btn-sign">New designer ? <span>sign up</span></a>

<main class="abs welcome">
  <h1>WELCOME TO ZEMBROLIA</h1>
  <p>Lorem ipsum dolor sit amet, consectetuer adipiscing elit, sed diam nonummy nibh euismod tincidunt ut laoreet dolore magna aliquam erat volutpat.</p>
  <p>Ut wisi enim ad minim veniam, quis nostrud exerci tation ullamcorper suscipit lobortis nisl ut aliquip ex ea commodo consequat. Duis autem vel eum iriure dolor in hendrerit in vulputate velit esse molestie consequat, vel illum dolore eu feugiat nulla facilisis at vero eros et accumsan et iusto odio dignissim qui blandit praesent luptatum zzril delenit augue duis dolore te feugait nulla facilisi.</p>
  <p class="narrow"><span>Nam liber tempor cum soluta nobis eleifend option congue nihil</span><span>placerat facer possim assum. Typi non habent claritatem insitam</span><span>eorum claritatem. Investigationes demonstraverunt lectores legere</span><span>Claritas est etiam processus dynamicus, qui sequitur mutationem</span><span>est notare quam littera gothica, quam nunc putamus parum claram</span><span>humanitatis per seacula quarta decima et quinta decima.</span></p>
  <p class="narrow" style="height:15px"><span>Eodem modo typi, qui nunc nobis videntur parum clari, fiant sollemnes</span></p>
</main>
<div class="abs piping" role="img" aria-label="Colourful icing piping bags"></div>
<a class="abs read-more">Read more</a>

<footer>
  <nav class="abs footnav">
    <a href="#">Home</a><a href="#">About us</a><a href="#">Products</a><a href="#">Specials</a><a href="#">Reviews</a><a href="#">FAQs</a><a href="#">Contact us</a>
  </nav>
  <p class="abs copyright">Copyright © 2012 Reserved</p>
  <div class="abs social" aria-label="Social links">
    <span style="background:#3b5a9a"></span><span style="background:#4aa6dc"></span><span style="background:#f07a22"></span><span style="background:#c9c9c9"></span>
  </div>
</footer>

</body>
</html>
```